Home inspection business! professional look attracting customers just by looks. Read must haves

its a new business I started on my own for home inspections I would like something very professional to give to real estate agents and clients, its going to have my license number on it my business phone number my name my website as well etc on the back side it will be servicing areas and also what kind of services I offer I also have a business card from someone else the way I would like mine to be. I will attach my logo

Home Inspection

listed in nice to haves

• phone number - 555 293 8471
• website- hollowpinecheck.com
• license number #2938475610
• my name Gavin keropulis
• picture of my logo and me on the front
• on the back of the card. stating I am servicing All of New York and Long Island
• also services I will offer will be home inspection -mold inspection -lead inspection -radon inspection -Termite Inspection -Infared Scan.
• and also we provide inspections for single family homes condos co-ops town-homes
• and commercial property
• same colors as the logos and also if you recommend fonts to look like the logo not sure up to you

```html
<!DOCTYPE html>
<html lang="en">
<head>
<meta charset="utf-8">
<title>Hollow Pine Home Inspectors – Business Card</title>
<link rel="stylesheet" href="https://fonts.googleapis.com/css2?family=Open+Sans:wght@400;600;700&display=swap">
<style>
  :root {
    --navy: #0d5579;
    --sky: #29a3dc;
    --paper: #ffffff;
    --ink: #555a5e;
    --canvas: #ffffff;
  }
  * { box-sizing: border-box; margin: 0; padding: 0; }
  html, body {
    width: 1200px; height: 1067px; overflow: hidden;
    background: var(--canvas);
    font-family: "Open Sans", Arial, sans-serif;
  }
  .card {
    position: absolute;
    left: 387px;
    width: 456px; height: 264px;
    background: var(--paper);
    border: 1px solid var(--navy);
    overflow: hidden;
  }
  .card--front { top: 184px; }
  .card--back  { top: 592px; }
  .card__shapes { position: absolute; inset: 0; width: 100%; height: 100%; }

  .brand {
    position: absolute; left: 56px; top: 97px;
    display: flex; align-items: center; gap: 5px;
    color: var(--navy); font-weight: 700;
  }
  .brand__dot { width: 14px; height: 14px; border-radius: 50%; background: var(--navy); flex: none; }
  .brand__name {
    font-size: 9.5px; line-height: 12px; letter-spacing: 0.05em;
    text-transform: uppercase; white-space: nowrap;
  }

  .owner {
    position: absolute; right: 20px; top: 88px;
    color: var(--sky); font-size: 14.5px; font-weight: 600;
    text-transform: uppercase; letter-spacing: 0.02em;
  }

  .contact {
    position: absolute; right: 14px; top: 180px;
    list-style: none; color: var(--ink); font-size: 12px; line-height: 19px; letter-spacing: 0.03em;
  }
  .contact li { display: flex; align-items: center; justify-content: flex-end; gap: 8px; }
  .contact svg { width: 10px; height: 10px; }

  .license {
    position: absolute; left: 45px; top: 237px;
    color: var(--paper); font-size: 12px; letter-spacing: 0.04em;
  }

  .coverage {
    position: absolute; left: 0; right: 0; top: 158px;
    text-align: center; color: var(--ink); font-size: 12px; line-height: 16px; letter-spacing: 0.03em;
  }
  .services {
    position: absolute; left: 0; right: 0; top: 222px;
    text-align: center; color: var(--paper); font-size: 12px; line-height: 15px; letter-spacing: 0.03em;
  }
</style>
</head>
<body>

<section class="card card--front" aria-label="Card front">
  <svg class="card__shapes" viewBox="0 0 456 264" preserveAspectRatio="none" aria-hidden="true">
    <polygon points="0,0 456,0 456,115 205,115 117,13 12,115 0,115" fill="var(--navy)"/>
    <rect x="0" y="228" width="456" height="36" fill="var(--sky)"/>
    <polygon points="26,228 238,228 258,264 10,264" fill="var(--navy)"/>
  </svg>
  <div class="brand">
    <span class="brand__dot"></span>
    <span class="brand__name">Hollow Pine<br>Home Inspectors</span>
  </div>
  <h1 class="owner">Gavin Keropulis</h1>
  <ul class="contact">
    <li>555 293 8471
      <svg viewBox="0 0 10 10"><path d="M2 0.5 L3.6 2.8 L2.7 3.8 C3.4 5.3 4.7 6.6 6.2 7.3 L7.2 6.4 L9.5 8 L8.5 9.5 C4.5 9.3 0.7 5.5 0.5 1.5 Z" fill="var(--sky)"/></svg>
    </li>
    <li>WWW.hollowpinecheck.com
      <svg viewBox="0 0 10 10"><circle cx="5" cy="5" r="4.3" fill="none" stroke="var(--sky)" stroke-width="1.2"/><ellipse cx="5" cy="5" rx="1.9" ry="4.3" fill="none" stroke="var(--sky)" stroke-width="1"/><line x1="0.7" y1="5" x2="9.3" y2="5" stroke="var(--sky)" stroke-width="1"/></svg>
    </li>
  </ul>
  <p class="license">license number #2938475610</p>
</section>

<section class="card card--back" aria-label="Card back">
  <svg class="card__shapes" viewBox="0 0 456 264" preserveAspectRatio="none" aria-hidden="true">
    <polygon points="0,0 456,0 456,115 205,115 117,13 12,115 0,115" fill="var(--navy)"/>
    <rect x="0" y="219" width="456" height="45" fill="var(--navy)"/>
  </svg>
  <div class="brand">
    <span class="brand__dot"></span>
    <span class="brand__name">Hollow Pine<br>Home Inspectors</span>
  </div>
  <h2 class="owner">Gavin Keropulis</h2>
  <p class="coverage">Servicing All of New York and Long Island<br>and also we provide inspections for single family homes<br>condos co-ops town-homes</p>
  <p class="services">home inspection -mold inspection -lead inspection<br>-radon inspection -Termite Inspection -Infared Scan</p>
</section>

</body>
</html>
```